Hawaiian Body Care Product Catalog for Wholesaling

Design a multi page catalog for a Hawaiian body care brand. There are about 6 different types of products (for example, soaps, lotions, lip balms) and we have about 50 products.

Catalog size: 5.5" x 8.5"

Please visit our website at www.corallumecare.example to get an idea of our product line and aesthetic. We would like to focus on the fun tropical fruit. This catalog to for sales reps to show retailers - so it's a wholesale catalog.

Target Market(s)

Retailers as were are wholesaling to them.

Industry/Entity Type

Beauty

Font styles to use
Sans Serif

Colors

Designer to choose colors to be used in the design.

Requirements
Must have
• Images of tropical fruit - we have a lot of stock images that I was unable to file transfer because it said they were too wide.
• Hi Res images for print.
Nice to have
• Images of each product per type of product. Descriptions of the products found on website. SKU under the images of each product. no pricing, just sku number. Playful images of tropical fruit, flowers and Hawaii. Somewhere we need to explain that we are donating 5% net profits to protect Hawaiian Wildlife, so maybe a page dedicated to that with an image of Hawaiian Wildlife.

```html
<!DOCTYPE html>
<html lang="en">
<head>
<meta charset="utf-8">
<title>Coral Lume Wholesale Catalog – Bar Soap Spread</title>
<link href="https://fonts.googleapis.com/css2?family=Source+Sans+3:wght@400;600;700&family=Great+Vibes&family=Libre+Caslon+Text&display=swap" rel="stylesheet">
<style>
  :root{
    --teal:#8fd0c6;
    --teal-deep:#7cc4b9;
    --white:#ffffff;
    --pink:#e3177b;
    --coral:#f07866;
    --sku:#f0b21c;
    --ink:#2d2d2d;
    --husk:#a0744a;
    --flesh:#f4f1ea;
  }
  *{box-sizing:border-box;margin:0;padding:0}
  html,body{width:1200px;height:1200px;overflow:hidden;background:var(--white)}
  body{position:relative;font-family:"Source Sans 3",Arial,sans-serif;color:var(--ink)}

  .spread{position:absolute;left:42px;top:42px;width:1114px;height:860px;background:var(--teal);overflow:hidden;box-shadow:4px 4px 8px rgba(0,0,0,.35)}
  .coconut{position:absolute;border-radius:50%}
  .coconut--husk{background:radial-gradient(circle,#c59a6a 0%,var(--husk) 70%)}
  .coconut--half{background:radial-gradient(circle,var(--flesh) 55%,#d9cfc0 70%,#8a6240 74%)}

  .spread-title{position:absolute;left:180px;top:18px;font-family:"Great Vibes",cursive;font-size:62px;color:var(--white);text-shadow:2px 3px 4px rgba(0,0,0,.25)}
  .intro{position:absolute;left:11px;top:88px;width:533px;height:52px;background:rgba(255,255,255,.45);color:var(--coral);font-size:12px;line-height:13.6px;text-align:center;padding-top:4px}

  .panel{position:absolute;background:var(--white);display:flex;flex-direction:column}
  .panel--left{left:11px;top:160px;width:533px;height:672px}
  .panel--right{left:568px;top:23px;width:534px;height:809px}

  .product{position:relative;flex:1;border-bottom:1.5px solid var(--pink)}
  .product:last-child{border-bottom:none}
  .product-photo{position:absolute;border-radius:2px}
  .panel--left .product-photo{left:25px;top:9px;width:68px;height:94px}
  .panel--right .product-photo{left:12px;top:8px;width:98px;height:92px}
  .product-sku{position:absolute;bottom:6px;color:var(--sku);font-size:13px}
  .panel--left .product-sku{left:13px}
  .panel--right .product-sku{left:13px}
  .product-info{position:absolute;top:2px}
  .panel--left .product-info{left:133px;width:360px}
  .panel--right .product-info{left:134px;width:370px}
  .product-name{color:var(--pink);font-weight:700;font-size:15.5px;line-height:18px}
  .product-scent{color:var(--coral);font-size:15px;line-height:17px}
  .product-desc{font-size:11.4px;line-height:13.6px;margin-top:2px}
  .panel--left .product-desc{margin-top:11px}
  .product-points{list-style:none;font-size:11.4px;line-height:13.6px}
  .product-points li::before{content:"• "}

  .caption{position:absolute;left:0;width:1200px;top:950px;text-align:center;font-family:"Libre Caslon Text",serif;font-size:54px;line-height:70px;color:#111}
</style>
</head>
<body>
<section class="spread">
  <div class="coconut coconut--husk" role="img" aria-label="Coconut husk photo" style="left:-60px;top:-40px;width:150px;height:150px"></div>
  <div class="coconut coconut--half" role="img" aria-label="Halved coconut photo" style="left:500px;top:-70px;width:170px;height:150px"></div>
  <div class="coconut coconut--half" role="img" aria-label="Halved coconut photo" style="left:300px;top:800px;width:160px;height:120px"></div>
  <div class="coconut coconut--husk" role="img" aria-label="Coconut husk photo" style="left:1040px;top:790px;width:120px;height:120px"></div>

  <h1 class="spread-title">Bar Soap</h1>
  <p class="intro">Treat your skin with ALOHA! Paraben-free, 100% Vegan and Cruelty-Free handmade Hawaiian<br>soaps enriched with moisturizing Kukui &amp; Coconut Oil. Pamper your skin and turn your<br>shower into a tropical retreat with these large 6 oz bar soaps made with real tropical fruit!</p>

  <div class="panel panel--left">
    <article class="product">
      <div class="product-photo" role="img" aria-label="Illustrated soap box with coconut and flowers" style="background:linear-gradient(160deg,#f3efe3,#9fd3c8 60%,#e9d9b8)"></div>
      <span class="product-sku">BS-2 Plumeria-1</span>
      <div class="product-info">
        <h2 class="product-name">Hawaiian Aromatherapy Pure Soap</h2>
        <p class="product-scent">Coconut Milk</p>
        <p class="product-desc">Bathe in Hawaiian Coconut Milk pure Hawaiian aromatherapy body soap made with moisturizing tropical oils and essential oils. 10% of net profits go towards protecting wildlife in Hawaii.</p>
      </div>
    </article>
    <article class="product">
      <div class="product-photo" role="img" aria-label="Illustrated soap box with hibiscus flowers" style="background:linear-gradient(160deg,#f4eee2,#f07a4a 55%,#6bab8e)"></div>
      <span class="product-sku">BS-2 Plumeria-1</span>
      <div class="product-info">
        <h2 class="product-name">Hawaiian Aromatherapy Pure Soap</h2>
        <p class="product-scent">Hibiscus Passion</p>
        <p class="product-desc">Bathe in Hawaiian Hibiscus Passion pure Hawaiian aromatherapy body soap made with moisturizing tropical oils and essential oils. 10% of net profits go towards protecting wildlife in Hawaii.</p>
      </div>
    </article>
    <article class="product">
      <div class="product-photo" role="img" aria-label="Illustrated soap box with honeycomb and flowers" style="background:linear-gradient(160deg,#f3efe3,#f3a93a 55%,#3c63a8)"></div>
      <span class="product-sku">BS-2 Plumeria-1</span>
      <div class="product-info">
        <h2 class="product-name">Hawaiian Aromatherapy Pure Soap</h2>
        <p class="product-scent">Honey Almond</p>
        <p class="product-desc">Bathe in Hawaiian Honey Almond pure Hawaiian aromatherapy body soap made with moisturizing tropical oils and essential oils. 10% of net profits go towards protecting wildlife in Hawaii.</p>
      </div>
    </article>
    <article class="product">
      <div class="product-photo" role="img" aria-label="Illustrated soap box with lavender sprigs" style="background:linear-gradient(160deg,#f1eee8,#9a86c2 55%,#e8663d)"></div>
      <span class="product-sku">BS-2 Plumeria-1</span>
      <div class="product-info">
        <h2 class="product-name">Hawaiian Aromatherapy Pure Soap</h2>
        <p class="product-scent">Lavender Fields</p>
        <p class="product-desc">Bathe in Hawaiian Lavender Fields pure Hawaiian aromatherapy body soap made with moisturizing tropical oils and essential oils. 10% of net profits go towards protecting wildlife in Hawaii.</p>
      </div>
    </article>
    <article class="product">
      <div class="product-photo" role="img" aria-label="Illustrated soap box with papaya and plumeria" style="background:linear-gradient(160deg,#f3efe3,#ee7a3a 55%,#e86a9a)"></div>
      <span class="product-sku">BS-2 Plumeria-1</span>
      <div class="product-info">
        <h2 class="product-name">Hawaiian Aromatherapy Pure Soap</h2>
        <p class="product-scent">Plumeria Nectar</p>
        <p class="product-desc">Indulge in absolute Hawaiian luxury with this pure Hawaiian aromatherapy cleansing body soap made with essential oils. 10% of net profits go towards protecting wildlife in Hawaii.</p>
      </div>
    </article>
  </div>

  <div class="panel panel--right">
    <article class="product">
      <div class="product-photo" role="img" aria-label="Clear and green soap bar with ginger flower" style="background:linear-gradient(90deg,#f2f2ee 45%,#49c5a0)"></div>
      <span class="product-sku">BS-2 Plumeria-1</span>
      <div class="product-info">
        <h2 class="product-name">Hawaiian Soap</h2>
        <p class="product-scent">Awapuhi with Kukui &amp; Coconut Oil</p>
        <p class="product-desc">Exotic, vigorous Hawaiian Awapuhi with a soft, cleansing ginger scent. Like swimming under a Hawaiian waterfall.</p>
        <ul class="product-points"><li>Made with Kukui, Coconut Oil &amp; real Tropical Fruit.</li><li>Moisturizing &amp; rich-lathering.</li><li>Softens and smoothes skin.</li><li>No phthalates &amp; 100% Vegan</li></ul>
      </div>
    </article>
    <article class="product">
      <div class="product-photo" role="img" aria-label="Cream soap bar with coconut half" style="background:linear-gradient(90deg,#e6cfa8 30%,#f4f1ea 50%,#e0c69a)"></div>
      <span class="product-sku">BS-2 Plumeria-1</span>
      <div class="product-info">
        <h2 class="product-name">Hawaiian Soap</h2>
        <p class="product-scent">Coconut with Kukui &amp; Coconut Oil</p>
        <p class="product-desc">A warm Hawaiian coconut aroma, accented with hints of sweet vanilla. A bestseller!</p>
        <ul class="product-points"><li>Made with Kukui, Coconut Oil &amp; real Tropical Fruit.</li><li>Moisturizing &amp; rich-lathering.</li><li>Softens and smoothes skin.</li><li>No phthalates &amp; 100% Vegan</li></ul>
      </div>
    </article>
    <article class="product">
      <div class="product-photo" role="img" aria-label="Green soap bar with gardenia flower" style="background:linear-gradient(90deg,#9ee06a 50%,#3cc25a)"></div>
      <span class="product-sku">BS-2 Plumeria-1</span>
      <div class="product-info">
        <h2 class="product-name">Hawaiian Soap</h2>
        <p class="product-scent">Gardenia with Kukui &amp; Coconut Oil</p>
        <p class="product-desc">Coral Lume Soap Co. Gardenia cleanser can make any day feel like springtime with it's sweet, earthy, floral scent of a gardenia in bloom.</p>
        <ul class="product-points"><li>Made with Kukui, Coconut Oil &amp; real Tropical Fruit.</li><li>Moisturizing &amp; rich-lathering.</li><li>Softens and smoothes skin.</li><li>No phthalates &amp; 100% Vegan</li></ul>
      </div>
    </article>
    <article class="product">
      <div class="product-photo" role="img" aria-label="Light and deep blue soap bar" style="background:linear-gradient(90deg,#bfe2f3 50%,#2f8fd8)"></div>
      <span class="product-sku">BS-2 Plumeria-1</span>
      <div class="product-info">
        <h2 class="product-name">Hawaiian Soap</h2>
        <p class="product-scent">Hawaiian Waters with Kukui &amp; Coconut Oil</p>
        <p class="product-desc">Hang ten on our invigorating, masculine Hawaiian Wave Kukui &amp; Coconut Oil Soap.</p>
        <ul class="product-points"><li>Made with Kukui, Coconut Oil &amp; real Tropical Fruit.</li><li>Moisturizing &amp; rich-lathering.</li><li>Softens and smoothes skin.</li><li>No phthalates &amp; 100% Vegan</li></ul>
      </div>
    </article>
    <article class="product">
      <div class="product-photo" role="img" aria-label="Clear soap bar with pink hibiscus and berries" style="background:linear-gradient(120deg,#f7c7d8,#f6f2f2 50%,#f39a6a)"></div>
      <span class="product-sku">BS-2 Plumeria-1</span>
      <div class="product-info">
        <h2 class="product-name">Hawaiian Soap</h2>
        <p class="product-scent">Hibiscus Berry with Kukui &amp; Coconut Oil</p>
        <p class="product-desc">A sublime medley of hibiscus petal and acai berry.</p>
        <ul class="product-points"><li>Made with Kukui, Coconut Oil &amp; real Tropical Fruit.</li><li>Moisturizing &amp; rich-lathering.</li><li>Softens and smoothes skin.</li><li>No phthalates &amp; 100% Vegan</li></ul>
      </div>
    </article>
    <article class="product">
      <div class="product-photo" role="img" aria-label="White soap bar with colorful cubes and starfish" style="background:linear-gradient(120deg,#f27aa0,#f4efe6 45%,#f2b03c)"></div>
      <span class="product-sku">BS-2 Plumeria-1</span>
      <div class="product-info">
        <h2 class="product-name">Hawaiian Soap</h2>
        <p class="product-scent">Island Sands with Kukui &amp; Coconut Oil</p>
        <p class="product-desc">With a design inspired by the Hawaiian rainbow, Island Sands Coral Lume Soap is a colorful combo of refreshing pineapple and sweet mango.</p>
        <ul class="product-points"><li>Made with Kukui, Coconut Oil &amp; real Tropical Fruit.</li><li>Moisturizing &amp; rich-lathering.</li><li>Softens and smoothes skin.</li><li>No phthalates &amp; 100% Vegan</li></ul>
      </div>
    </article>
  </div>
</section>

<p class="caption">Page 3 &amp; 4 spread<br>sample</p>
</body>
</html>
```